Ductless Mini Split Business Website

Tall Fern Services is looking to design an eye catching educational website about installing Ductless mini splits.

Similar to this company.
https://www.kelvarocomfort.com/

```html
<!DOCTYPE html>
<html lang="en">
<head>
<meta charset="utf-8">
<title>Tall Fern Services – Ductless Experts</title>
<link href="https://fonts.googleapis.com/css2?family=Luckiest+Guy&family=Arimo:wght@400;700&display=swap" rel="stylesheet">
<style>
:root{
  --yellow:#f0b412;
  --yellow-soft:#f7d277;
  --ink:#1d1d1d;
  --text:#777;
  --dark:#2a2a2a;
  --white:#fff;
  --line:#e6e6e6;
}
*{box-sizing:border-box;margin:0;padding:0}
html,body{width:1200px;height:4488px;overflow:hidden;background:var(--white)}
body{position:relative;font-family:"Arimo",Arial,sans-serif;color:var(--text)}
.abs{position:absolute}
.display{font-family:"Luckiest Guy",cursive;color:var(--ink);font-weight:400;letter-spacing:1px}
.para{font-size:11.5px;line-height:19.5px;color:var(--text)}
.btn{position:absolute;display:flex;align-items:center;justify-content:center;background:var(--yellow);color:var(--white);font-family:"Luckiest Guy",cursive;font-size:15px;border-radius:4px;letter-spacing:.5px}
.ph{position:absolute}

/* hero */
.hero-band{left:0;top:0;width:833px;height:638px;background:var(--yellow);border-bottom-right-radius:40px}
.logo{left:134px;top:0;width:202px;height:105px;background:var(--white);border-radius:0 0 60px 60px;display:flex;flex-direction:column;align-items:center;justify-content:center}
.logo-name{font-family:"Arimo",sans-serif;font-weight:700;font-size:17px;color:var(--ink)}
.logo-sub{font-family:"Arimo",sans-serif;font-weight:700;font-size:13px;color:var(--ink);margin-top:4px}
.nav{top:38px;left:0;width:1200px;height:20px}
.nav span{position:absolute;font-size:12px;color:var(--ink)}
.hero-title{left:162px;top:205px;font-size:58px;line-height:68px}
.hero-text{left:162px;top:352px;width:450px;color:var(--white)}
.hero-btn{left:162px;top:428px;width:186px;height:51px;background:var(--white);color:var(--ink);font-size:18px}
.hero-photo{left:657px;top:94px;width:411px;height:486px;border-radius:16px;background:linear-gradient(160deg,#d9dde2,#9aa3ad 55%,#3a5ea8)}
.hero-badge{left:880px;top:505px;width:130px;height:148px;background:var(--yellow);clip-path:polygon(50% 0,100% 25%,100% 75%,50% 100%,0 75%,0 25%)}

/* sections */
.section-title{font-size:36px}
.center{left:0;width:1200px;text-align:center}
.help-bg{left:0;top:1185px;width:1200px;height:627px;background:linear-gradient(180deg,#fff,#f3f3f3 40%,#f4f1ee 70%,#fff)}
.service{position:absolute;width:200px;text-align:center}
.service h3{font-size:13px;color:var(--ink);font-weight:700;margin:12px 0 6px}
.service p{font-size:11px;line-height:19px;color:var(--text)}
.icon{display:block;margin:0 auto;width:52px;height:52px}

.card{position:absolute;background:var(--white);box-shadow:0 2px 10px rgba(0,0,0,.12);border-radius:4px;text-align:center;padding:0 18px}
.card h3{font-size:12.5px;color:var(--ink);font-weight:700;margin:10px 0 6px}
.card p{font-size:10.5px;line-height:18.5px}

.svc-card{position:absolute;width:186px;height:187px;background:var(--white);box-shadow:0 2px 10px rgba(0,0,0,.14);border-radius:3px}
.svc-card .img{position:absolute;left:8px;top:8px;width:170px;height:140px}
.svc-card .label{position:absolute;left:8px;bottom:12px;right:8px;font-size:12px;font-weight:700;color:var(--ink)}
.svc-card .arrow{position:absolute;right:10px;bottom:12px;color:var(--yellow);font-weight:700;font-size:13px}

.field{position:absolute;border:1px solid var(--line);font-size:11.5px;color:#666;padding:12px 16px}

/* footer */
.footer{left:0;top:4029px;width:1200px;height:422px;background:var(--dark);border-radius:22px 22px 0 0}
.foot-h{font-size:15px;color:var(--yellow)}
.foot-list{font-size:11.5px;line-height:19.6px;color:#e6e6e6}
.copyright{left:0;top:4451px;width:1200px;height:37px;background:var(--yellow);color:var(--white);font-size:11px;display:flex;align-items:center;justify-content:center}
.social{position:absolute;top:4353px;width:32px;height:32px;border-radius:3px}
</style>
</head>
<body>

<!-- hero -->
<div class="abs hero-band"></div>
<div class="abs logo">
  <div class="logo-name">Tall Fern Services</div>
  <div class="logo-sub">DUCTLESS EXPERTS</div>
</div>
<nav class="abs nav">
  <span style="left:428px">Home</span>
  <span style="left:499px">About Us</span>
  <span style="left:585px">Ductless Heat Pumps</span>
  <span style="left:746px">FAQ</span>
  <span style="left:803px">Financing</span>
  <span style="left:891px">Reviews</span>
  <span style="left:970px">Contact Us</span>
</nav>
<h1 class="abs display hero-title">Tall Fern Ductless<br>Services</h1>
<p class="abs para hero-text">Lorem Ipsum is simply dummy text of the printing and typesetting industry. Lorem Ipsum has been the industry's standard dummy text.</p>
<div class="btn hero-btn">Get In Touch</div>
<div class="ph hero-photo" role="img" aria-label="Technician on a ladder installing a wall-mounted ductless unit while a customer watches"></div>
<div class="ph hero-badge" role="img" aria-label="Honeycomb badge with a cartoon bee"></div>

<svg class="abs" style="left:360px;top:640px" width="620" height="540" viewBox="0 0 620 540" fill="none">
  <path d="M10 80 C40 10,200 20,320 40 S560 60,600 20" stroke="#333" stroke-width="1.2" stroke-dasharray="2 4"/>
  <path d="M40 440 C60 480,80 500,80 540" stroke="#333" stroke-width="1.2" stroke-dasharray="2 4"/>
</svg>

<!-- about -->
<svg class="abs" style="left:168px;top:760px" width="400" height="370" viewBox="0 0 400 370">
  <path d="M60 40 C140 0,260 10,340 60 C400 100,400 240,360 290 C300 360,160 380,80 330 C10 290,0 200,10 140 C18 90,30 60,60 40Z" fill="#f0b412"/>
  <path d="M80 60 C160 20,270 40,330 90 C380 140,370 250,320 300 C260 350,140 350,80 300 C20 250,10 160,40 110 C50 90,60 72,80 60Z" fill="#c9ccd0"/>
</svg>
<div class="ph" style="left:290px;top:720px;width:140px;height:110px;border-radius:50%;background:#f0b412" role="img" aria-label="Cartoon bee illustration"></div>
<div class="ph" style="left:248px;top:830px;width:270px;height:260px;border-radius:45%;background:linear-gradient(140deg,#e9ecef,#b7bcc2)" role="img" aria-label="Technician servicing an indoor ductless unit"></div>
<h2 class="abs display section-title" style="left:611px;top:762px">About Us</h2>
<p class="abs para" style="left:611px;top:826px;width:430px">Lorem Ipsum is simply dummy text of the printing and typesetting industry. Lorem Ipsum has been the industry's standard dummy text ever since the 1500s, when an unknown printer took a galley of type and scrambled it to make a type specimen book.</p>
<p class="abs para" style="left:611px;top:924px;width:430px">It was popularised in the 1960s with the release of Letraset sheets containing Lorem Ipsum passages, and more recently with desktop publishing software like Aldus PageMaker including versions of Lorem Ipsum</p>
<div class="btn" style="left:611px;top:1031px;width:119px;height:40px">Read More</div>

<!-- help -->
<div class="abs help-bg"></div>
<h2 class="abs display section-title center" style="top:1220px">How Can We Help You?</h2>

<div class="service" style="left:243px;top:1325px">
  <svg class="icon" viewBox="0 0 52 52" fill="none" stroke="#f0b412" stroke-width="2"><circle cx="32" cy="24" r="16" fill="#fbe6ad" stroke="none"/><rect x="10" y="8" width="30" height="34" rx="4"/><circle cx="25" cy="25" r="9"/><path d="M25 16v18M21 17v16M29 17v16"/></svg>
  <h3>Baseboard Heat Replacement</h3><p>Lorem Ipsum is simply dummy text of the printing and typesetting industry.</p>
</div>
<div class="service" style="left:498px;top:1325px">
  <svg class="icon" viewBox="0 0 52 52" fill="none" stroke="#f0b412" stroke-width="2"><circle cx="32" cy="24" r="16" fill="#fbe6ad" stroke="none"/><path d="M10 8h32v8H30v28h-8V16H10z"/></svg>
  <h3>Ductless Heat Pump FAQ</h3><p>Lorem Ipsum is simply dummy text of the printing and typesetting industry.</p>
</div>
<div class="service" style="left:754px;top:1325px">
  <svg class="icon" viewBox="0 0 52 52" fill="none" stroke="#f0b412" stroke-width="2"><circle cx="32" cy="24" r="16" fill="#fbe6ad" stroke="none"/><path d="M8 12h32v12H28l-4 14h-8l4-14H8z"/></svg>
  <h3>Ductless Installation</h3><p>Lorem Ipsum is simply dummy text of the printing and typesetting industry.</p>
</div>
<div class="service" style="left:243px;top:1520px">
  <svg class="icon" viewBox="0 0 52 52" fill="none" stroke="#f0b412" stroke-width="2"><circle cx="32" cy="24" r="16" fill="#fbe6ad" stroke="none"/><circle cx="20" cy="30" r="9"/><circle cx="20" cy="30" r="3"/><circle cx="36" cy="16" r="7"/><circle cx="36" cy="16" r="2"/></svg>
  <h3>Ductless Maintenance</h3><p>Lorem Ipsum is simply dummy text of the printing and typesetting industry.</p>
</div>
<div class="service" style="left:498px;top:1520px">
  <svg class="icon" viewBox="0 0 52 52" fill="none" stroke="#f0b412" stroke-width="2"><circle cx="32" cy="24" r="16" fill="#fbe6ad" stroke="none"/><path d="M26 6l16 6v12c0 10-8 16-16 20-8-4-16-10-16-20V12z"/><path d="M19 25l5 5 9-9"/></svg>
  <h3>Ductless Warranty</h3><p>Lorem Ipsum is simply dummy text of the printing and typesetting industry.</p>
</div>
<div class="service" style="left:754px;top:1520px">
  <svg class="icon" viewBox="0 0 52 52" fill="none" stroke="#f0b412" stroke-width="2"><circle cx="32" cy="24" r="16" fill="#fbe6ad" stroke="none"/><rect x="8" y="18" width="36" height="24" rx="3"/><path d="M14 22v16M20 22v16M26 22v16M32 22v16M38 22v16M14 8v6M20 8v6M26 8v6M32 8v6M38 8v6"/></svg>
  <h3>Whole House Ductless</h3><p>Lorem Ipsum is simply dummy text of the printing and typesetting industry.</p>
</div>
<div class="btn" style="left:537px;top:1719px;width:127px;height:40px">Explore More</div>

<!-- quality -->
<h2 class="abs display section-title" style="left:162px;top:1870px">Quality Work Guarantee</h2>
<p class="abs para" style="left:162px;top:1941px;width:430px">Lorem Ipsum is simply dummy text of the printing and typesetting industry. Lorem Ipsum has been the industry's standard dummy text ever since the 1500s, when an unknown printer took a galley of type and scrambled it to make a type specimen book.</p>
<p class="abs para" style="left:162px;top:2039px;width:430px">It was popularised in the 1960s with the release of Letraset sheets containing Lorem Ipsum passages, and more recently with desktop publishing software like Aldus PageMaker including versions of Lorem Ipsum</p>
<div class="btn" style="left:162px;top:2153px;width:118px;height:40px">Read More</div>
<svg class="abs" style="left:620px;top:1800px" width="580" height="480" viewBox="0 0 580 480" fill="none">
  <path d="M5 10 C20 180,120 470,360 470" stroke="#333" stroke-width="1.2" stroke-dasharray="2 4"/>
  <circle cx="428" cy="248" r="248" fill="#f0b412"/>
</svg>
<div class="ph" style="left:830px;top:1808px;width:420px;height:460px;border-radius:50%;background:linear-gradient(160deg,#e6ebef,#b6c2cc 60%,#8a97a3)" role="img" aria-label="Outdoor heat pump unit with two cartoon bees"></div>

<!-- why choose -->
<div class="card" style="left:160px;top:2280px;width:220px;height:201px;padding-top:30px">
  <svg width="56" height="56" viewBox="0 0 56 56" fill="none" stroke="#f0b412" stroke-width="2"><circle cx="36" cy="28" r="16" fill="#fbe6ad" stroke="none"/><rect x="12" y="8" width="26" height="36" rx="3"/><path d="M18 18h14M18 26h14M18 34h10"/></svg>
  <h3>0% Financing for 60 months</h3><p>Lorem Ipsum is simply dummy text of the printing and typesetting industry.</p>
</div>
<div class="card" style="left:160px;top:2498px;width:220px;height:200px;padding-top:28px">
  <svg width="56" height="56" viewBox="0 0 56 56" fill="none" stroke="#f0b412" stroke-width="2"><circle cx="36" cy="26" r="16" fill="#fbe6ad" stroke="none"/><circle cx="28" cy="16" r="8"/><path d="M28 12v8M6 40l10-6h14l10-6M6 48h30l14-10"/></svg>
  <h3>365 Day, Money Back Guarantee</h3><p>Lorem Ipsum is simply dummy text of the printing and typesetting industry.</p>
</div>
<div class="card" style="left:397px;top:2390px;width:220px;height:200px;padding-top:28px">
  <svg width="56" height="56" viewBox="0 0 56 56" fill="none" stroke="#f0b412" stroke-width="2"><circle cx="36" cy="26" r="16" fill="#fbe6ad" stroke="none"/><circle cx="20" cy="22" r="10"/><circle cx="34" cy="34" r="10"/></svg>
  <h3>We Are the Experts in Services</h3><p>Lorem Ipsum is simply dummy text of the printing and typesetting industry.</p>
</div>
<h2 class="abs display section-title" style="left:664px;top:2375px">Why Choose Us?</h2>
<p class="abs para" style="left:664px;top:2445px;width:340px">Lorem Ipsum is simply dummy text of the printing and typesetting industry. Lorem Ipsum has been the industry's standard dummy text ever since the 1500s, when an unknown printer took a galley of type and scrambled it to make a type specimen book.</p>
<div class="btn" style="left:664px;top:2575px;width:127px;height:40px">Discover Now</div>

<!-- testimonials -->
<svg class="abs" style="left:0;top:2755px" width="460" height="500" viewBox="0 0 460 500">
  <path d="M0 30 C120 -10,300 40,400 150 C470 230,450 370,360 420 C260 480,90 500,0 480Z" fill="#222"/>
  <path d="M0 50 C110 20,280 60,370 160 C430 230,420 350,340 395 C250 445,90 460,0 440Z" fill="#f0b412"/>
</svg>
<div class="ph" style="left:-14px;top:2752px;width:46px;height:46px;border-radius:50%;background:#c7c2bd;border:3px solid #fff" role="img" aria-label="Client portrait"></div>
<div class="ph" style="left:157px;top:2892px;width:64px;height:64px;border-radius:50%;background:#b9bcc0;border:3px solid #fff" role="img" aria-label="Client portrait"></div>
<div class="ph" style="left:360px;top:2890px;width:48px;height:48px;border-radius:50%;background:#b9bcc0;border:3px solid #fff" role="img" aria-label="Client portrait"></div>
<div class="ph" style="left:188px;top:3190px;width:88px;height:88px;border-radius:50%;background:#9fa4aa;border:4px solid #fff" role="img" aria-label="Client portrait"></div>
<div class="abs" style="left:20px;top:2975px;width:370px;text-align:center;color:#fff">
  <div style="font-size:13px;color:var(--ink);font-weight:700">- Client Name</div>
  <p style="font-size:10.5px;line-height:19px;margin-top:6px;padding:0 10px">Lorem Ipsum is simply dummy text of the printing and typesetting industry. Lorem Ipsum has been the industry's standard dummy text ever since the 1500s, when an unknown printer took a galley of type and scrambled it to make a type specimen book.</p>
</div>
<div class="abs" style="left:20px;top:2950px;color:#fff;font-size:34px;font-family:Georgia,serif">&ldquo;</div>
<div class="abs" style="left:345px;top:3090px;color:#fff;font-size:34px;font-family:Georgia,serif">&rdquo;</div>
<svg class="abs" style="left:135px;top:3132px" width="85" height="12"><circle cx="6" cy="6" r="3" fill="#fff"/><circle cx="42" cy="6" r="4" fill="#fff"/><circle cx="78" cy="6" r="3" fill="#fff"/></svg>
<h2 class="abs display section-title" style="left:533px;top:2962px">What Our Client Say</h2>
<p class="abs para" style="left:533px;top:3032px;width:320px">Lorem Ipsum is simply dummy text of the printing and typesetting industry. Lorem Ipsum has been the industry's standard dummy text ever since the 1500s.</p>

<!-- our services -->
<h2 class="abs display section-title" style="left:162px;top:3352px">Our Services</h2>
<p class="abs para" style="left:162px;top:3408px;width:230px">Lorem Ipsum is simply dummy text of the printing and typesetting industry. Lorem Ipsum has been the industry's standard dummy text ever since the 1500s.</p>
<div class="svc-card" style="left:446px;top:3334px"><div class="img" role="img" aria-label="Woman adjusting a wall unit with a remote" style="background:linear-gradient(160deg,#f1f3f5,#c8ccd1)"></div><div class="label">Get Some Answers</div><div class="arrow">&#10140;</div></div>
<div class="svc-card" style="left:656px;top:3334px"><div class="img" role="img" aria-label="Hands counting banknotes" style="background:linear-gradient(160deg,#a7b4aa,#6f7d78)"></div><div class="label">Our Financing Options</div><div class="arrow">&#10140;</div></div>
<div class="svc-card" style="left:866px;top:3334px"><div class="img" role="img" aria-label="Technician servicing a ceiling unit" style="background:linear-gradient(160deg,#eef1f4,#8ea4c4)"></div><div class="label">Stay Up To Date</div><div class="arrow">&#10140;</div></div>

<!-- contact -->
<h2 class="abs display section-title center" style="top:3580px">Contact Us</h2>
<div class="field" style="left:286px;top:3667px;width:306px;height:44px">Name:</div>
<div class="field" style="left:608px;top:3667px;width:306px;height:44px">Email:</div>
<div class="field" style="left:286px;top:3728px;width:306px;height:44px">Phone:</div>
<div class="field" style="left:608px;top:3728px;width:306px;height:44px">Services:
  <svg style="position:absolute;right:16px;top:17px" width="12" height="8"><path d="M0 0h12L6 8z" fill="#f0b412"/></svg></div>
<div class="field" style="left:286px;top:3789px;width:628px;height:127px">Message:</div>
<div class="btn" style="left:530px;top:3925px;width:148px;height:40px">Drop A Message</div>

<!-- footer -->
<div class="abs footer"></div>
<div class="abs" style="left:162px;top:4132px;font-size:18px;font-weight:700;color:var(--yellow)">Tall Fern Services</div>
<div class="abs" style="left:162px;top:4160px;font-size:13px;font-weight:700;color:var(--yellow)">DUCTLESS EXPERTS</div>
<p class="abs foot-list" style="left:162px;top:4200px;width:200px">Lorem Ipsum is simply dummy text of the printing and typesetting industry. Lorem Ipsum has been the industry's standard dummy text ever since the 1500s, when an unknown printer took a galley of type.</p>
<div class="abs foot-h" style="left:387px;top:4107px">Quick Link</div>
<div class="abs foot-list" style="left:387px;top:4154px">Home<br>About Us<br>Ductless Heat Pumps<br>FAQ<br>Financing<br>Reviews<br>Contact Us</div>
<div class="abs foot-h" style="left:613px;top:4107px">Services</div>
<div class="abs foot-list" style="left:613px;top:4154px">Get Some Answers<br>Our Financing Options<br>Stay Up To Date</div>
<div class="abs foot-h" style="left:838px;top:4107px">Contact Info</div>
<svg class="abs" style="left:838px;top:4156px" width="20" height="20" viewBox="0 0 20 20" fill="none" stroke="#f0b412" stroke-width="1.8"><path d="M4 2l4 4-2 3c1 2 3 4 5 5l3-2 4 4-3 3C8 18 2 12 1 5z"/></svg>
<div class="abs" style="left:868px;top:4150px;font-size:10.5px;line-height:16px;color:#eee">Customer Service:<br>+91-000-000-0000</div>
<svg class="abs" style="left:838px;top:4210px" width="20" height="16" viewBox="0 0 20 16" fill="none" stroke="#f0b412" stroke-width="1.8"><rect x="1" y="1" width="18" height="14"/><path d="M1 1l9 8 9-8"/></svg>
<div class="abs" style="left:868px;top:4204px;font-size:10.5px;line-height:16px;color:#eee">Email:<br>info@tallfernservices.com</div>
<svg class="abs" style="left:838px;top:4262px" width="18" height="22" viewBox="0 0 18 22" fill="none" stroke="#f0b412" stroke-width="1.8"><path d="M9 21s8-8 8-13A8 8 0 0 0 1 8c0 5 8 13 8 13z"/><circle cx="9" cy="8" r="3"/></svg>
<div class="abs" style="left:868px;top:4258px;font-size:10.5px;line-height:16px;color:#eee">Address:<br>100-Lorem ipsum is simply dum..</div>
<div class="social" style="left:517px;background:#3b5998"></div>
<div class="social" style="left:561px;background:#dd4b39"></div>
<div class="social" style="left:606px;background:#0077b5"></div>
<div class="social" style="left:651px;background:#1da1f2"></div>
<div class="abs copyright">© Copyright -2019 Tall Fern Services. Terms &amp; Conditions | Privacy policy</div>

</body>
</html>
```